Animal Horse & Bedding Company Needs a Website Coded & Designed

We need a website for a new animal bedding and feed company that is visually grabbing and vibrant. We would like to see a website that displays trust, quality and confidence. Needs to be responsive and mobile friendly for all browsers and coded for both Android & IOS. SEO is also important.

Joomla or Wordpress – must be both desktop and mobile friendly with fast page load speed. Need the ability to edit ourselves in Wordpress or Joomla.

Full details attached below with some layout and content ideas.

Coding

Coded - Design and coding required

Number of Pages Required

5+ page

Font styles to use
Sans Serif

Requirements
Must have
• Needs to be responsive and mobile friendly for all browsers and coded for both Android & IOS. SEO is also important.

Wordpress – must be both desktop and mobile friendly with fast page load speed. Need the ability to edit ourselves in Wordpress.

Logo Colours:
Dark Brown
CMYK: 50 / 70 / 80 / 70
Pantone: 4625C

Orange
CMYK: 0 / 50 / 100 / 0
Pantone: 144C
Nice to have
• Use picture of building attached and super impose logo on building.

```html
<!DOCTYPE html>
<html lang="en">
<head>
<meta charset="utf-8">
<title>Golden Sheaf – Bedding &amp; Feed</title>
<link href="https://fonts.googleapis.com/css2?family=Montserrat:wght@400;500;600;700&display=swap" rel="stylesheet">
<style>
:root{
  --orange:#e8821e;
  --orange-light:#f39a2c;
  --brown-dark:#3d1a0f;
  --brown-mid:#6b3218;
  --nav:#3a2a22;
  --ink:#1f1f1f;
  --muted:#6f6f6f;
  --line:#e6e6e6;
  --bg:#f2f2f2;
  --white:#ffffff;
}
*{margin:0;padding:0;box-sizing:border-box}
html,body{width:1200px;height:3158px;overflow:hidden}
body{background:var(--bg);font-family:'Montserrat',sans-serif;color:var(--ink)}
.page{position:absolute;left:191px;top:44px;width:818px;height:3070px;background:var(--white);box-shadow:0 10px 40px rgba(0,0,0,.18);overflow:hidden}
section,header,footer{position:absolute;left:0;width:818px}
.btn{position:absolute;background:var(--orange);color:var(--white);font-size:8px;font-weight:600;text-transform:uppercase;display:flex;align-items:center;justify-content:center;letter-spacing:.3px;white-space:nowrap}

/* hero */
.hero{top:0;height:403px;background:linear-gradient(100deg,#7a5a2c 0%,#a77a32 30%,#c08c34 55%,#a96a24 80%,#7d4a1a 100%)}
.hero-photo{position:absolute;inset:0;background:radial-gradient(ellipse 220px 200px at 640px 200px,rgba(140,60,20,.55),transparent 70%),linear-gradient(180deg,rgba(60,45,30,.35) 0%,rgba(0,0,0,0) 40%,rgba(90,60,20,.25) 100%)}
.brand{position:absolute;display:flex;flex-direction:column;align-items:center;color:var(--white);white-space:nowrap}
.brand-mark{width:26px;height:26px;border-radius:50%;border:2px solid var(--white);margin-bottom:6px}
.brand-name{font-size:19px;font-weight:500;letter-spacing:1.2px;text-transform:uppercase;white-space:nowrap}
.brand-tag{font-size:7px;letter-spacing:5px;margin-top:3px;white-space:nowrap}
.hero .brand{left:80px;top:8px;width:170px}
.topbar{position:absolute;top:10px;left:455px;display:flex;gap:28px;font-size:8px;color:var(--white);align-items:center;white-space:nowrap}
.topbar span{display:flex;align-items:center;gap:8px}
.quote-tab{position:absolute;top:0;left:733px;width:85px;height:38px;background:var(--orange);color:var(--white);font-size:7.5px;line-height:1.1;display:flex;align-items:center}
.quote-tab .arrow{width:18px;height:38px;background:rgba(0,0,0,.25);display:flex;align-items:center;justify-content:center;margin-right:10px}
.mainnav{position:absolute;top:38px;left:345px;width:473px;height:41px;background:rgba(50,38,30,.82);display:flex}
.mainnav a{flex:1;color:var(--white);font-size:10px;text-decoration:none;display:flex;align-items:center;justify-content:center;border-right:1px solid rgba(255,255,255,.18)}
.mainnav a:last-child{border-right:none}
.hero h1{position:absolute;left:78px;top:147px;font-size:30px;line-height:35px;font-weight:700;color:var(--white);text-transform:uppercase;white-space:nowrap}
.hero h1 em{font-style:normal;color:var(--orange-light)}
.hero .sub{position:absolute;left:84px;top:234px;font-size:19px;line-height:24px;font-weight:500;color:var(--white);text-transform:uppercase;white-space:nowrap}
.hero .btn{left:84px;top:284px;width:117px;height:30px;font-size:8.5px}
.dots{position:absolute;left:86px;top:340px;display:flex;gap:9px;align-items:center}
.dots i{width:7px;height:7px;border-radius:50%;background:var(--orange-light)}
.dots i.on{width:11px;height:11px;border:2px solid var(--orange-light);background:transparent}

/* intro */
.intro{top:403px;height:357px}
.tile{position:absolute;width:135px;height:111px}
.intro h2{position:absolute;left:357px;top:76px;font-size:21px;line-height:22px;font-weight:700;white-space:nowrap}
.intro p{position:absolute;left:357px;width:380px;font-size:7.6px;line-height:13.4px;color:var(--muted)}
.intro .btn{left:357px;top:267px;width:96px;height:21px}

/* benefits */
.benefits{color:var(--white)}
.benefits h2{position:absolute;font-size:19px;font-weight:700;text-transform:uppercase;white-space:nowrap}
.benefits .rule{position:absolute;height:2px;background:var(--orange);width:134px}
.benefits ul{position:absolute;list-style:none}
.benefits li{position:relative;padding-left:16px;font-size:12px;white-space:nowrap}
.benefits li::before{content:"";position:absolute;left:0;top:6px;width:5px;height:5px;border-radius:50%;background:var(--orange)}
.bedding{top:760px;height:354px;background:linear-gradient(100deg,#4a1f12 0%,#6e3018 35%,#8c4620 60%,#5a2814 100%)}
.bedding h2{left:81px;top:48px}
.bedding .rule{left:81px;top:82px}
.bedding ul{left:84px;top:106px}
.bedding li{height:25.5px}
.bedding .btn{left:97px;top:284px;width:94px;height:20px}
.feed{top:1844px;height:362px;background:linear-gradient(90deg,#3a2410 0%,#5c3e18 35%,#6b3c14 60%,#4a2510 100%)}
.feed h2{left:420px;top:52px}
.feed ul{left:420px;top:110px}
.feed li{height:20.9px;font-size:11.5px}
.feed .btn{left:436px;top:306px;width:94px;height:20px}

/* products */
.products{top:1114px;height:730px}
.section-title{position:absolute;left:0;width:818px;text-align:center;font-size:20px;font-weight:600}
.card{position:absolute;width:182px;height:228px;background:var(--white);box-shadow:0 2px 10px rgba(0,0,0,.16)}
.price{position:absolute;left:-8px;top:10px;width:105px;height:30px;background:var(--orange);border-radius:0 15px 15px 0;color:var(--white);font-size:13px;font-style:italic;display:flex;align-items:center;padding-left:20px}
.pack{position:absolute;left:50px;top:52px;width:82px;height:92px;border-radius:4px}
.card .name{position:absolute;left:16px;top:170px;font-size:8px;font-weight:600;text-transform:uppercase;white-space:nowrap}
.card .stars{position:absolute;right:22px;top:167px;font-size:9px;color:var(--orange);letter-spacing:1px}
.card .fav{position:absolute;left:16px;top:192px;width:18px;height:18px;border:1px solid var(--orange);display:flex;align-items:center;justify-content:center}
.card .btn{left:42px;top:193px;width:75px;height:16px;font-size:6px}
.corner{position:absolute;right:-6px;bottom:-6px;width:0;height:0;border-left:34px solid transparent;border-bottom:34px solid var(--orange)}
.products .viewall{left:359px;top:679px;width:94px;height:22px}

/* testimonials */
.testimonials{top:2206px;height:540px}
.testimonials .rule{position:absolute;left:357px;top:102px;width:100px;height:2px;background:var(--orange)}
.quote{position:absolute;top:150px;width:210px;height:269px;background:var(--white);box-shadow:0 2px 12px rgba(0,0,0,.14);text-align:center}
.quote .stars{margin-top:30px;font-size:13px;color:var(--orange);letter-spacing:2px}
.quote p{margin:8px 24px 0;font-size:8.4px;line-height:14.4px;color:#333}
.avatar{width:45px;height:45px;border-radius:50%;background:linear-gradient(160deg,#c9c3bd,#7d7570);margin:14px auto 0}
.quote .who{margin-top:13px;font-size:8.4px;font-weight:600}
.quote .where{margin-top:10px;font-size:7px;color:var(--orange)}
.testimonials .btn{left:366px;top:469px;width:96px;height:21px}

/* newsletter + footer */
.footer{top:2798px;height:272px;background:var(--brown-dark);color:var(--white)}
.newsletter{position:absolute;left:53px;top:2744px;width:741px;height:76px;background:var(--orange);z-index:2}
.newsletter label{position:absolute;left:29px;top:30px;font-size:11px;color:var(--white);white-space:nowrap}
.newsletter .field{position:absolute;left:198px;top:20px;width:368px;height:39px;background:var(--white);font-size:10px;color:#777;display:flex;align-items:center;padding-left:10px}
.newsletter .go{position:absolute;left:566px;top:18px;width:108px;height:41px;background:#2a140c;color:var(--white);font-size:11px;display:flex;align-items:center;justify-content:center}
.footer .brand{left:44px;top:44px;width:130px}
.footer .brand-name{font-size:14px;letter-spacing:1px}
.footer .brand-mark{width:20px;height:20px;margin-bottom:4px}
.footer .brand-tag{font-size:5px;letter-spacing:4px}
.footer .about{position:absolute;left:44px;top:108px;width:160px;font-size:7.6px;line-height:13px;color:#e8dcd6}
.socials{position:absolute;left:55px;top:190px;display:flex;gap:23px}
.socials i{width:11px;height:11px;border-radius:50%;border:1.5px solid var(--white)}
.fcol{position:absolute;top:68px;white-space:nowrap}
.fcol h3{font-size:12.5px;font-weight:500;text-transform:uppercase;margin-bottom:8px}
.fcol ul{list-style:none}
.fcol li{position:relative;padding-left:22px;font-size:8px;color:#eadfd9}
.fcol li::before{content:"";position:absolute;left:0;top:4px;width:4px;height:4px;border-radius:50%;background:var(--orange)}
.col-products{left:246px}
.col-products li{height:16.4px}
.col-care{left:392px}
.col-care li{height:20.5px}
.col-call{left:584px;top:64px}
.col-call .call{font-size:14px}
.col-call .phone{font-size:14px;color:var(--orange);margin-top:7px}
.col-call .row{display:flex;align-items:center;gap:16px;font-size:13px;margin-top:20px}
.footer .divider{position:absolute;left:44px;top:243px;width:730px;height:1px;background:rgba(255,255,255,.2)}
.footer .legal{position:absolute;left:0;top:252px;width:818px;text-align:center;font-size:8px;color:#e8dcd6}
</style>
</head>
<body>
<div class="page">

  <header class="hero">
    <div class="hero-photo" role="img" aria-label="Chestnut horse galloping across a golden grass field"></div>
    <div class="brand">
      <span class="brand-mark"></span>
      <span class="brand-name">Golden Sheaf</span>
      <span class="brand-tag">BEDDING &amp; FEED</span>
    </div>
    <div class="topbar">
      <span><svg width="10" height="10" viewBox="0 0 24 24" fill="#fff"><path d="M6.6 10.8a15 15 0 0 0 6.6 6.6l2.2-2.2a1 1 0 0 1 1-.25 11.4 11.4 0 0 0 3.6.57 1 1 0 0 1 1 1V20a1 1 0 0 1-1 1A17 17 0 0 1 3 4a1 1 0 0 1 1-1h3.5a1 1 0 0 1 1 1c0 1.25.2 2.45.57 3.57a1 1 0 0 1-.25 1z"/></svg>555-0188-742</span>
      <span><svg width="12" height="9" viewBox="0 0 24 18" fill="#fff"><path d="M2 0h20a2 2 0 0 1 2 2v14a2 2 0 0 1-2 2H2a2 2 0 0 1-2-2V2a2 2 0 0 1 2-2zm0 3v1l10 6 10-6V3L12 9z"/></svg>goldensheaf.com</span>
    </div>
    <div class="quote-tab"><span class="arrow"><svg width="7" height="9" viewBox="0 0 7 10"><path d="M1 1l4 4-4 4" stroke="#fff" stroke-width="2" fill="none"/></svg></span>Request a<br>Quote</div>
    <nav class="mainnav">
      <a>Home</a><a>Feed</a><a>Beeding</a><a>About Us</a><a>Contact us</a>
    </nav>
    <h1>Welcome to <em>Animals</em><br><em>Bedding</em> Company</h1>
    <p class="sub">Happy pets make life<br>better!</p>
    <span class="btn">Request a quote</span>
    <div class="dots"><i class="on"></i><i></i><i></i><i></i><i></i></div>
  </header>

  <section class="intro">
    <div class="tile" style="left:46px;top:74px;background:linear-gradient(160deg,#6e8a3a,#8a6a42)" role="img" aria-label="Rabbit sitting in green grass"></div>
    <div class="tile" style="left:192px;top:74px;background:linear-gradient(160deg,#d9b08a,#b98a5a)" role="img" aria-label="Piglets resting on straw"></div>
    <div class="tile" style="left:46px;top:194px;background:linear-gradient(160deg,#8a8a88,#3c3c3e)" role="img" aria-label="Grey cat eating from a bowl"></div>
    <div class="tile" style="left:192px;top:194px;background:linear-gradient(160deg,#e8e2d4,#8c8a5e)" role="img" aria-label="Lamb lying on grass"></div>
    <h2>The bedding that’s kind to<br>your animals</h2>
    <p style="top:136px">Your animal deserves the very best in health and comfort to keep them healthy, strong and happy. Our products are designed for horses, livestock (goats, cattle and sheep), small caged animals (rabbits, guinea pigs and more).Your animal deserves the very best in health and comfort to keep them healthy, strong and happy. Our products are designed for horses, livestock (goats, cattle and sheep), small caged animals (rabbits, guinea pigs and more).</p>
    <p style="top:218px">QUALITY GUARANTEED: Grown for quality - 100% natural with no chemicals or additives<br>FULL SERVICE SOLUTION</p>
    <span class="btn">Learn more</span>
  </section>

  <section class="benefits bedding" role="img" aria-label="White horse running through an autumn paddock">
    <h2>Bedding Benefits</h2>
    <span class="rule"></span>
    <ul>
      <li>100% Natural Chopped Straw</li>
      <li>Low Dust</li>
      <li>Chemical &amp; Additive Free</li>
      <li>Clean &amp; Highly Absorbent</li>
      <li>Cheaper than Wood Shavings</li>
      <li>Economic – less used and less wasted</li>
      <li>Environmentally Friendly – Recyclable &amp; Compostable</li>
    </ul>
    <span class="btn">Learn more</span>
  </section>

  <section class="products">
    <h2 class="section-title" style="top:52px">Our Products</h2>

    <div class="card" style="left:85px;top:141px"><span class="price">$109.00</span><div class="pack" style="background:linear-gradient(180deg,#2a66b8 0 22%,#a63aa0 22%)" role="img" aria-label="Pet food tin"></div><span class="name">Marina Blend</span><span class="stars">★★★★★</span><span class="fav"><svg width="9" height="8" viewBox="0 0 24 21"><path d="M12 20S2 13.5 2 7a5 5 0 0 1 10-1 5 5 0 0 1 10 1c0 6.5-10 13-10 13z" stroke="#e8821e" stroke-width="2.4" fill="none"/></svg></span><span class="btn">Add to card</span><span class="corner"></span></div>
    <div class="card" style="left:321px;top:141px"><span class="price">$109.00</span><div class="pack" style="background:linear-gradient(180deg,#e04030,#c8302a 60%,#2a6ab0)" role="img" aria-label="Horse muesli feed bag"></div><span class="name">Trail Muesli</span><span class="stars">★★★★★</span><span class="fav"><svg width="9" height="8" viewBox="0 0 24 21"><path d="M12 20S2 13.5 2 7a5 5 0 0 1 10-1 5 5 0 0 1 10 1c0 6.5-10 13-10 13z" stroke="#e8821e" stroke-width="2.4" fill="none"/></svg></span><span class="btn">Add to card</span><span class="corner"></span></div>
    <div class="card" style="left:558px;top:141px"><span class="price">$109.00</span><div class="pack" style="background:linear-gradient(180deg,#dfe3ea,#b6c0cf 60%,#2b4a8a)" role="img" aria-label="Digestive care feed bag"></div><span class="name">Marina Blend</span><span class="stars">★★★★★</span><span class="fav"><svg width="9" height="8" viewBox="0 0 24 21"><path d="M12 20S2 13.5 2 7a5 5 0 0 1 10-1 5 5 0 0 1 10 1c0 6.5-10 13-10 13z" stroke="#e8821e" stroke-width="2.4" fill="none"/></svg></span><span class="btn">Add to card</span><span class="corner"></span></div>

    <div class="card" style="left:85px;top:401px"><span class="price">$109.00</span><div class="pack" style="background:linear-gradient(180deg,#2a66b8 0 22%,#a63aa0 22%)" role="img" aria-label="Pet food tin"></div><span class="name">Marina Blend</span><span class="stars">★★★★★</span><span class="fav"><svg width="9" height="8" viewBox="0 0 24 21"><path d="M12 20S2 13.5 2 7a5 5 0 0 1 10-1 5 5 0 0 1 10 1c0 6.5-10 13-10 13z" stroke="#e8821e" stroke-width="2.4" fill="none"/></svg></span><span class="btn">Add to card</span><span class="corner"></span></div>
    <div class="card" style="left:321px;top:401px"><span class="price">$109.00</span><div class="pack" style="background:linear-gradient(180deg,#e04030,#c8302a 60%,#2a6ab0)" role="img" aria-label="Horse muesli feed bag"></div><span class="name">Trail Muesli</span><span class="stars">★★★★★</span><span class="fav"><svg width="9" height="8" viewBox="0 0 24 21"><path d="M12 20S2 13.5 2 7a5 5 0 0 1 10-1 5 5 0 0 1 10 1c0 6.5-10 13-10 13z" stroke="#e8821e" stroke-width="2.4" fill="none"/></svg></span><span class="btn">Add to card</span><span class="corner"></span></div>
    <div class="card" style="left:558px;top:401px"><span class="price">$109.00</span><div class="pack" style="background:linear-gradient(180deg,#dfe3ea,#b6c0cf 60%,#2b4a8a)" role="img" aria-label="Digestive care feed bag"></div><span class="name">Marina Blend</span><span class="stars">★★★★★</span><span class="fav"><svg width="9" height="8" viewBox="0 0 24 21"><path d="M12 20S2 13.5 2 7a5 5 0 0 1 10-1 5 5 0 0 1 10 1c0 6.5-10 13-10 13z" stroke="#e8821e" stroke-width="2.4" fill="none"/></svg></span><span class="btn">Add to card</span><span class="corner"></span></div>

    <span class="btn viewall">View all</span>
  </section>

  <section class="benefits feed" role="img" aria-label="Brown hare sitting in a golden meadow">
    <h2>Bedding Benefits</h2>
    <ul>
      <li>100% Natural</li>
      <li>Chemical &amp; Additive Free</li>
      <li>Available in Pellets or Cubes</li>
      <li>High Protein Content</li>
      <li>Eliminate Waste In Feeding</li>
      <li>Clean - Eliminates Dust From Feeding Baled Hay</li>
      <li>Cost Effective</li>
      <li>Convenient</li>
      <li>Less wasted feed</li>
    </ul>
    <span class="btn">Learn more</span>
  </section>

  <section class="testimonials">
    <h2 class="section-title" style="top:70px;font-weight:500;text-transform:uppercase">Testimonial</h2>
    <span class="rule"></span>
    <div class="quote" style="left:35px"><div class="stars">★★★★★</div><p>lorem ipsum dolor sit amet, consectetur adipiscing elit. nulla sed cum nunc, egestas placerat vulputate id vitae. a id pellentesque suspendisse tortor mi elementum interdum mauris venenatis.</p><div class="avatar" role="img" aria-label="Customer portrait"></div><div class="who">DANA WHITFIELD</div><div class="where">MINNEPOLIS.MN</div></div>
    <div class="quote" style="left:302px"><div class="stars">★★★★★</div><p>lorem ipsum dolor sit amet, consectetur adipiscing elit. nulla sed cum nunc, egestas placerat vulputate id vitae. a id pellentesque suspendisse tortor mi elementum interdum mauris venenatis.</p><div class="avatar" role="img" aria-label="Customer portrait"></div><div class="who">DANA WHITFIELD</div><div class="where">MINNEPOLIS.MN</div></div>
    <div class="quote" style="left:568px"><div class="stars">★★★★★</div><p>lorem ipsum dolor sit amet, consectetur adipiscing elit. nulla sed cum nunc, egestas placerat vulputate id vitae. a id pellentesque suspendisse tortor mi elementum interdum mauris venenatis.</p><div class="avatar" role="img" aria-label="Customer portrait"></div><div class="who">DANA WHITFIELD</div><div class="where">MINNEPOLIS.MN</div></div>
    <span class="btn">Learn more</span>
  </section>

  <div class="newsletter">
    <label>Subscribe Our Newsletter</label>
    <span class="field">Enter your email</span>
    <span class="go">Subscribe</span>
  </div>

  <footer class="footer">
    <div class="brand">
      <span class="brand-mark"></span>
      <span class="brand-name">Golden Sheaf</span>
      <span class="brand-tag">BEDDING &amp; FEED</span>
    </div>
    <p class="about">The Golden Sheaf is a locally owned company located in Pine Hollow, AB. We are dedicated in providing high quality products and services.</p>
    <div class="socials"><i></i><i></i><i></i><i></i></div>

    <div class="fcol col-products"><h3>Products</h3><ul><li>Cats</li><li>Dog</li><li>Rabit</li><li>Birds</li><li>sheep</li><li>pigs</li></ul></div>
    <div class="fcol col-care"><h3>Customer Care</h3><ul><li>Home</li><li>Our Services</li><li>blog</li><li>About us</li><li>Contact Us</li></ul></div>
    <div class="fcol col-call">
      <div class="call">Call Now For Services!</div>
      <div class="phone">555-014-2276</div>
      <div class="row" style="margin-top:24px"><svg width="14" height="11" viewBox="0 0 24 18"><rect x="1" y="1" width="22" height="16" rx="1" stroke="#fff" stroke-width="1.6" fill="none"/><path d="M1 2l11 8 11-8" stroke="#fff" stroke-width="1.6" fill="none"/></svg>Email Us</div>
      <div class="row"><svg width="12" height="15" viewBox="0 0 20 26"><path d="M10 25S2 15 2 9a8 8 0 0 1 16 0c0 6-8 16-8 16z" stroke="#fff" stroke-width="1.8" fill="none"/><circle cx="10" cy="9" r="3" stroke="#fff" stroke-width="1.8" fill="none"/></svg>Get Direction</div>
    </div>
    <span class="divider"></span>
    <p class="legal">Golden Sheaf © 2021 All Rights Reserved. Terms of Use and Privacy Policy</p>
  </footer>

</div>
</body>
</html>
```